Business Card - high end, modern health care

Hey designers!

We need a double sided business card for the boutique, cutting edge physical therapy rehabilitation centre in Sydney's Northern Beaches.

With the most qualified physios in the area The Ridgeline Motion Clinic does what other physiotherapy practices do not, we take our time with our patients giving them longer appointments, better physios and therefor faster results!

We guarantee that the service people receive at TRMC will be unparalleled.

Hence we need a business card to reflect our modern, boutique, high end service. The final design needs to reflect that we are in a class of our own yet with the feel of beachside retreat.

Below I have attached our logo in both blue on white and white on blue. The exact colour is;
and the font that we have used in our logo is Tex Gyre Aventador.

I like the idea of the blue as the main colour as it is more eye catching and our signage onto the main road will be in this blue and in the interest of consistency across marketing the blue needs to be a part of the design. However I would appreciate a few designs onto a wooden background as this is a visual theme within the fitout of the practice.

The design needs to be of standard size (91x55mm).

Target Market(s)

We target people who have an end outcome in mind and those who have had poor experiences with other providers and ensure that everyone gets the care that they deserve with a premium service that is tailored to the individuals circumstances. As a premium service, the target market is highly educated, business and tech savvy with the additional target market of elderly people who have self funded their retirement and see value in paying for the best ongoing rehabilitation to maintain independence.

Industry/Entity Type

Physical Therapy

Contact Information for Business Card

Name, designation( Titled Musculoskeletal Physiotherapist... there will also be those in the company that have multiple designations ie 5 or 6 words long), phone number, email, facebook, instagram, address

Font styles to use
Sans Serif

Colors

Designer to choose colors to be used in the design.

Requirements
Must have
• Front - The logo as large as possible, blue or wooden theme, and all of the important details.
• Back - A blank space/lines on which to write appointment times (no "Appointment, date, time" etc.)
Nice to have
• facebook url
• logos for facebook and instagram
• Mini logos for the phone and email?

```html
<!DOCTYPE html>
<html lang="en">
<head>
<meta charset="utf-8">
<title>The Ridgeline Motion Clinic — Business Card</title>
<link rel="stylesheet" href="https://fonts.googleapis.com/css2?family=Roboto:wght@400;500;700&family=Roboto+Condensed:wght@500;700&family=Source+Sans+3:wght@400&display=swap">
<style>
  :root {
    --backdrop: #2b2b2b;
    --card: #f3f3f3;
    --card-back: #ffffff;
    --brand-blue: #0d56a6;
    --band-grey: #55585c;
    --text-grey: #4a4a4a;
    --rule-grey: #6a6a6a;
    --divider: #b9b9b9;
    --faint-blue: #eef2f8;
  }
  * { margin: 0; padding: 0; box-sizing: border-box; }
  html, body { width: 1200px; height: 960px; overflow: hidden; }
  body { background: var(--backdrop); position: relative; font-family: "Roboto", sans-serif; }

  .card { position: absolute; width: 598px; height: 342px; border-radius: 18px; overflow: hidden; }
  .card-front { left: 322px; top: 108px; background: var(--card); }
  .card-back { left: 320px; top: 493px; width: 600px; background: var(--card-back); }

  /* Front */
  .brand { position: absolute; left: 70px; top: 132px; display: flex; align-items: center; gap: 8px; }
  .brand-dot { width: 38px; height: 38px; border-radius: 50%; background: var(--brand-blue); flex: none; }
  .brand-name { color: var(--brand-blue); font-family: "Roboto", sans-serif; font-weight: 700; font-size: 19px; line-height: 1.05; text-transform: uppercase; letter-spacing: 0.2px; }

  .divider { position: absolute; left: 327px; top: 68px; width: 2px; height: 180px; background: linear-gradient(to bottom, transparent, var(--divider) 15%, var(--divider) 85%, transparent); }

  .details { position: absolute; left: 354px; top: 64px; color: var(--text-grey); }
  .person-name { font-family: "Roboto Condensed", sans-serif; font-weight: 700; font-size: 21px; color: var(--brand-blue); line-height: 1.1; }
  .person-title { font-family: "Roboto Condensed", sans-serif; font-weight: 500; font-size: 15px; color: var(--text-grey); margin-top: 2px; }
  .address { font-size: 14px; line-height: 19px; margin-top: 10px; }
  .contact-list { list-style: none; margin-top: 9px; font-size: 14px; line-height: 19px; }
  .contact-list li { display: flex; align-items: center; gap: 9px; }
  .contact-list svg { width: 13px; height: 13px; flex: none; }

  .web-band { position: absolute; left: 0; top: 299px; width: 100%; height: 30px; background: var(--band-grey); }
  .web-band-blue { position: absolute; left: 0; top: 0; width: 465px; height: 100%; background: var(--brand-blue); }
  .web-address { position: absolute; left: 81px; top: 6px; color: #fff; font-size: 14px; letter-spacing: 5.2px; }
  .band-badge { position: absolute; left: 447px; top: -2px; width: 34px; height: 34px; border-radius: 50%; background: var(--brand-blue); border: 2px solid #fff; }

  /* Back */
  .watermark { position: absolute; left: 150px; top: 37px; width: 300px; height: 300px; border-radius: 50%; border: 22px solid var(--faint-blue); }
  .appt-form { position: absolute; inset: 0; font-family: "Source Sans 3", sans-serif; color: var(--text-grey); font-size: 17px; }
  .field { position: absolute; display: flex; align-items: flex-end; gap: 3px; }
  .field-line { border-bottom: 1px solid var(--rule-grey); height: 1px; margin-bottom: 5px; }
  .row-name { left: 32px; top: 40px; width: 527px; }
  .row-name .field-line { flex: 1; }
  .row-date { left: 32px; top: 82px; width: 527px; }
  .write-line { position: absolute; left: 35px; width: 524px; border-top: 1px solid var(--rule-grey); }
</style>
</head>
<body>

<section class="card card-front" aria-label="Business card front">
  <div class="brand">
    <span class="brand-dot"></span>
    <span class="brand-name">The Ridgeline<br>Motion Clinic</span>
  </div>

  <div class="divider"></div>

  <div class="details">
    <h1 class="person-name">DANIEL HARPER</h1>
    <p class="person-title">CEO/FOUNDER</p>
    <p class="address">4210 Heron Bay Road<br>Seaview, Oregon 97214</p>
    <ul class="contact-list">
      <li>
        <svg viewBox="0 0 24 24"><path fill="var(--brand-blue)" d="M6.6 10.8a15.1 15.1 0 0 0 6.6 6.6l2.2-2.2c.3-.3.7-.4 1-.2 1.1.4 2.3.6 3.6.6.6 0 1 .4 1 1V20c0 .6-.4 1-1 1A17 17 0 0 1 3 4c0-.6.4-1 1-1h3.5c.6 0 1 .4 1 1 0 1.3.2 2.5.6 3.6.1.3 0 .7-.2 1z"/></svg>
        555 018 2947
      </li>
      <li>
        <svg viewBox="0 0 24 24"><rect x="2" y="5" width="20" height="14" rx="1" fill="var(--brand-blue)"/><path d="M3 6l9 7 9-7" fill="none" stroke="#fff" stroke-width="1.6"/></svg>
        daniel@ridgelinemotion.com
      </li>
      <li>
        <svg viewBox="0 0 24 24"><rect x="2" y="2" width="20" height="20" rx="2" fill="var(--brand-blue)"/></svg>
        /ridgelinemotion
      </li>
      <li>
        <svg viewBox="0 0 24 24"><rect x="2" y="2" width="20" height="20" rx="4" fill="var(--brand-blue)"/></svg>
        @ridgelinemotion
      </li>
    </ul>
  </div>

  <div class="web-band">
    <div class="web-band-blue"></div>
    <span class="web-address">www.ridgelinemotion.com</span>
    <span class="band-badge"></span>
  </div>
</section>

<section class="card card-back" aria-label="Business card back">
  <div class="watermark"></div>
  <div class="appt-form">
    <div class="field row-name"><span>Name</span><span class="field-line"></span></div>
    <div class="field row-date">
      <span>Date</span><span class="field-line" style="width:261px"></span>
      <span style="margin-left:5px">Time</span><span class="field-line" style="width:115px"></span>
      <span style="margin-left:3px">am/pm</span>
    </div>
    <span class="write-line" style="top:139px"></span>
    <span class="write-line" style="top:179px"></span>
    <span class="write-line" style="top:219px"></span>
    <span class="write-line" style="top:259px"></span>
    <span class="write-line" style="top:299px"></span>
  </div>
</section>

</body>
</html>
```